Business cards Marta Kessel Sport & Events

I need new business cards to match my new logo design for my company called "Marta Kessel Sport & Events". I'm based in Germany.
With my company, I offer different services in the context of sport.

Marta Kessel owner

Marta Kessel Sports & Events
Birkenfelder Weg 12
D-63118 Offenbach

+49 69 / 31 52 94 07
info@marta-kessel.example
www.marta-kessel.example

Contact Information for Business Card

Marta Kessel Inhaberin Marta Kessel Sport & Events Birkenfelder Weg 12 D-63118 Offenbach +49 69 / 31 52 94 07 info@marta-kessel.example www.marta-kessel.example

Requirements
Must have
• Logo | Double sided business card

```html
<!DOCTYPE html>
<html lang="de">
<head>
<meta charset="utf-8">
<title>Marta Kessel Sport &amp; Events – Visitenkarten</title>
<link rel="stylesheet" href="https://fonts.googleapis.com/css2?family=Michroma&family=Archivo+Black&family=Arimo:wght@400;700&display=swap">
<style>
  :root {
    --ink: #161414;
    --orange: #f6a01e;
    --accent-red: #e2411f;
    --white: #ffffff;
    --page: #e9e7e4;
  }
  * { margin: 0; padding: 0; box-sizing: border-box; }
  html, body { width: 1200px; height: 892px; overflow: hidden; }
  body {
    background: var(--page);
    display: flex;
    align-items: center;
    justify-content: center;
    gap: 40px;
  }
  .card {
    width: 540px;
    height: 350px;
    position: relative;
    overflow: hidden;
    background: var(--ink);
    box-shadow: 0 6px 22px rgba(0,0,0,.18);
  }
  .card svg.card-shape { position: absolute; inset: 0; }

  /* Front side */
  .brand-mark {
    position: absolute;
    left: 42px; top: 95px;
    width: 140px; height: 140px;
    border-radius: 50%;
    background: var(--orange);
  }
  .brand-name-small {
    position: absolute;
    left: 0; width: 224px; top: 252px;
    text-align: center;
    font-family: "Michroma", sans-serif;
    font-size: 12px;
    color: var(--white);
    letter-spacing: .5px;
  }
  .contact-block {
    position: absolute;
    left: 318px; top: 52px; right: 18px;
    color: var(--ink);
    font-family: "Arimo", sans-serif;
  }
  .role-line {
    font-family: "Archivo Black", sans-serif;
    font-size: 12px;
    padding-bottom: 6px;
    border-bottom: 1px solid rgba(22,20,20,.45);
    margin-bottom: 10px;
  }
  .company-name {
    font-family: "Michroma", sans-serif;
    font-size: 15.5px;
    line-height: 1;
  }
  .company-tag {
    font-family: "Michroma", sans-serif;
    font-size: 6.5px;
    letter-spacing: 4px;
    color: var(--accent-red);
    margin: 3px 0 10px 30px;
  }
  .address, .contact-list { font-size: 12.5px; line-height: 1.4; }
  .contact-list { list-style: none; margin-top: 8px; }
  .contact-list b { display: inline-block; width: 16px; font-weight: 700; }

  /* Back side */
  .back .brand-mark { left: 330px; top: 55px; width: 110px; height: 110px; }
  .back-wordmark {
    position: absolute;
    left: 0; right: 0; top: 190px;
    text-align: center;
    color: var(--white);
    font-family: "Michroma", sans-serif;
  }
  .back-wordmark .name { font-size: 30px; letter-spacing: 1px; }
  .back-wordmark .tag { font-size: 11px; letter-spacing: 9px; margin-top: 8px; }
</style>
</head>
<body>

<section class="card front" aria-label="Visitenkarte Vorderseite">
  <svg class="card-shape" viewBox="0 0 540 350" width="540" height="350" aria-hidden="true">
    <rect x="150" y="0" width="390" height="350" fill="var(--orange)"/>
    <circle cx="110" cy="165" r="205" fill="var(--white)"/>
    <circle cx="110" cy="165" r="193" fill="var(--ink)"/>
    <rect x="0" y="0" width="150" height="350" fill="var(--ink)"/>
  </svg>
  <div class="brand-mark" aria-hidden="true"></div>
  <p class="brand-name-small">Marta Kessel</p>

  <div class="contact-block">
    <p class="role-line">Marta Kessel Inhaberin</p>
    <p class="company-name">MARTA KESSEL</p>
    <p class="company-tag">SPORT &amp; EVENTS</p>
    <p class="address">Birkenfelder Weg 12<br>D-63118 Offenbach</p>
    <ul class="contact-list">
      <li><b>T</b>+49 69 / 31 52 94 07</li>
      <li><b>E</b>info@marta-kessel.example</li>
      <li><b>W</b>www.marta-kessel.example</li>
    </ul>
  </div>
</section>

<section class="card back" aria-label="Visitenkarte Rückseite">
  <div class="brand-mark" aria-hidden="true"></div>
  <div class="back-wordmark">
    <p class="name">MARTA KESSEL</p>
    <p class="tag">SPORT &amp; EVENTS</p>
  </div>
</section>

</body>
</html>
```